A3 Event Poster for School Fundraiser

We are looking for a bold, engaging, and professional A3 poster design to promote a special school fundraising event. A top athlete will be visiting a primary school to inspire children, encourage participation in sport, and help launch a fundraising initiative to raise money for new PE/sports equipment for the school.

The poster will be displayed prominently outside the school and shared with parents and families. Its purpose is to generate excitement, explain the event quickly, and encourage parents/families to sponsor and get involved.

We work with about 50 different athletes so will need the design to be easy to alter the picture of the athlete/name etc so it can be replicated across the different athletes.

Target Market(s)

Priamary School Parents/Communities

Industry/Entity Type

Education

Font styles to use
Other font styles liked:
• The logo font is Rajdhani. ‘Corvel’ is bold, ‘Pennix’ is semibold and the strapline is regular.

Requirements
Must have
• Space for the Event Date (that school can write in themselves), A picture of the visiting athlete and their bio (with ability to easily change)
Nice to have
• Bold, eye-catching

```html
<!DOCTYPE html>
<html lang="en">
<head>
<meta charset="utf-8">
<title>Corvel Pennix – Inspirational Athlete Visiting Our School</title>
<link rel="stylesheet" href="https://fonts.googleapis.com/css2?family=Rajdhani:wght@400;500;600;700&family=Russo+One&family=Roboto:wght@300;400;700&display=swap">
<style>
  :root {
    --white: #ffffff;
    --royal: #2b2f8f;
    --blue: #1f55c4;
    --sky: #1fb6ee;
    --red: #e41f35;
    --pink: #d83c9f;
    --pink-soft: #e283be;
    --purple: #6c2a8c;
    --ink: #2a2f86;
  }
  * { box-sizing: border-box; margin: 0; padding: 0; }
  html, body { width: 893px; height: 1200px; overflow: hidden; background: var(--white); }
  .poster { position: relative; width: 893px; height: 1200px; overflow: hidden; background: var(--white); font-family: "Rajdhani", sans-serif; }
  .backdrop { position: absolute; inset: 0; }
  .brand { position: absolute; left: 54px; top: 34px; display: flex; align-items: center; gap: 12px; }
  .brand-dot { width: 40px; height: 40px; border-radius: 50%; background: var(--red); }
  .brand-name { font-family: "Rajdhani", sans-serif; font-weight: 700; font-size: 52px; line-height: 1; color: var(--purple); letter-spacing: .5px; }
  .kicker { position: absolute; left: 70px; top: 255px; font-family: "Rajdhani", sans-serif; font-weight: 700; font-size: 46px; color: var(--pink-soft); line-height: 1; }
  .headline { position: absolute; left: 56px; top: 299px; font-family: "Russo One", sans-serif; font-weight: 400; font-size: 86px; color: var(--white); line-height: 1; letter-spacing: 1px; }
  .tagline { position: absolute; left: 78px; top: 403px; font-family: "Rajdhani", sans-serif; font-weight: 700; font-size: 35px; color: var(--white); line-height: 1; letter-spacing: .5px; }
  .role { position: absolute; left: 56px; top: 486px; display: flex; align-items: center; gap: 22px; }
  .role-text { font-family: "Rajdhani", sans-serif; font-weight: 500; font-size: 43px; color: var(--white); line-height: 42px; }
  .bio { position: absolute; left: 58px; top: 602px; width: 382px; font-family: "Roboto", sans-serif; font-weight: 300; font-size: 17px; line-height: 23.5px; color: var(--white); }
  .athlete-name { position: absolute; left: 806px; top: 0; width: 57px; height: 430px; display: flex; align-items: center; justify-content: center; }
  .athlete-name span { transform: rotate(-90deg); font-family: "Russo One", sans-serif; font-size: 52px; color: var(--white); white-space: nowrap; }
  .appeal { position: absolute; left: 57px; top: 781px; font-family: "Rajdhani", sans-serif; font-weight: 700; font-size: 37px; line-height: 33px; color: var(--white); }
  .value { position: absolute; width: 160px; text-align: center; font-family: "Rajdhani", sans-serif; font-weight: 700; font-size: 26px; line-height: 25px; color: var(--white); }
  .event-date { position: absolute; left: 63px; top: 1018px; width: 776px; height: 62px; border: 2px solid var(--ink); border-radius: 10px; overflow: hidden; background: var(--white); }
  .event-date-panel { position: absolute; left: 0; top: 0; }
  .event-date-label { position: absolute; left: 18px; top: 0; height: 100%; display: flex; align-items: center; gap: 14px; font-family: "Rajdhani", sans-serif; font-weight: 700; font-size: 37px; color: var(--white); }
  .mission { position: absolute; left: 0; right: 0; top: 1153px; text-align: center; font-family: "Roboto", sans-serif; font-weight: 700; font-size: 25px; color: var(--white); }
</style>
</head>
<body>
<main class="poster">
  <svg class="backdrop" width="893" height="1200" viewBox="0 0 893 1200" aria-hidden="true">
    <defs>
      <linearGradient id="blueWash" x1="0" y1="1" x2="1" y2="0">
        <stop offset="0" stop-color="#2b2f8f"/>
        <stop offset=".5" stop-color="#1f55c4"/>
        <stop offset="1" stop-color="#1fb6ee"/>
      </linearGradient>
      <linearGradient id="photoWash" x1="0" y1="0" x2="1" y2="1">
        <stop offset="0" stop-color="#c9cbe6"/>
        <stop offset=".55" stop-color="#5a4f9c"/>
        <stop offset="1" stop-color="#1c2a6e"/>
      </linearGradient>
      <pattern id="dots" width="10" height="10" patternUnits="userSpaceOnUse">
        <circle cx="5" cy="5" r="2.2" fill="#ffffff" opacity=".55"/>
      </pattern>
    </defs>
    <!-- blue splash field -->
    <path fill="url(#blueWash)"
      d="M0 262 L40 238 L70 226 L110 214 L150 200 L200 186 L250 176 L300 164 L360 150 L420 132 L470 118 L520 98 L560 86 L600 70 L640 56 L690 40 L740 26 L790 14 L830 4 L893 0 L893 714 L600 728 L300 740 L0 748 Z"/>
    <path fill="url(#dots)" d="M440 620 L893 600 L893 714 L440 734 Z"/>
    <!-- athlete portrait -->
    <circle cx="755" cy="418" r="256" fill="none" stroke="var(--red)" stroke-width="46"/>
    <circle cx="755" cy="418" r="234" fill="url(#photoWash)" role="img" aria-label="Portrait of the visiting athlete in team jacket"/>
    <!-- purple name band -->
    <rect x="806" y="0" width="57" height="430" fill="var(--purple)"/>
    <!-- red fundraising band -->
    <path fill="var(--red)" d="M0 746 L300 737 L600 725 L893 712 L893 915 L600 932 L300 950 L0 969 Z"/>
    <path fill="url(#dots)" d="M0 885 L200 874 L200 955 L0 969 Z"/>
    <path fill="url(#dots)" d="M760 720 L893 714 L893 800 L760 810 Z"/>
    <!-- dividers -->
    <g stroke="#ffffff" stroke-width="1.5" fill="none">
      <line x1="354" y1="754" x2="338" y2="930"/>
      <line x1="537" y1="754" x2="519" y2="869"/>
      <line x1="712" y1="754" x2="694" y2="869"/>
      <line x1="56" y1="476" x2="288" y2="476"/>
      <line x1="56" y1="582" x2="424" y2="582"/>
    </g>
    <!-- tagline brush band -->
    <path fill="var(--pink)" d="M58 402 L112 399 L412 399 L438 410 L418 420 L447 428 L418 434 L430 442 L110 444 L60 441 L70 424 L53 414 Z"/>
    <!-- value icons -->
    <g>
      <circle cx="439" cy="811" r="48" fill="#ffffff" stroke="var(--royal)" stroke-width="7"/>
      <circle cx="618" cy="799" r="48" fill="#ffffff" stroke="var(--royal)" stroke-width="7"/>
      <circle cx="790" cy="787" r="48" fill="#ffffff" stroke="var(--royal)" stroke-width="7"/>
      <g fill="none" stroke="var(--royal)" stroke-width="2.2" stroke-linecap="round" stroke-linejoin="round">
        <path d="M424 791 h30 v10 a15 15 0 0 1 -30 0 z M424 795 h-6 a8 8 0 0 0 8 10 M454 795 h6 a8 8 0 0 1 -8 10 M439 816 v8 M430 831 h18 M432 824 h14 v7"/>
        <path d="M439 797 l2 4 4 .5 -3 3 .8 4 -3.8 -2 -3.8 2 .8 -4 -3 -3 4 -.5 z"/>
        <path d="M618 810 l-10 -10 a6 6 0 0 1 10 -7 a6 6 0 0 1 10 7 z"/>
        <path d="M598 792 v16 l10 10 v6 M638 792 v16 l-10 10 v6"/>
        <circle cx="803" cy="771" r="5"/>
        <path d="M797 781 l-14 -4 -8 6 M797 781 l-8 14 10 8 -4 12 M789 795 l-10 8 -12 -2 M799 780 l8 8 8 -2"/>
      </g>
    </g>
    <!-- footer band -->
    <path fill="var(--purple)" d="M0 1138 L120 1134 L300 1136 L500 1132 L700 1134 L893 1132 L893 1200 L0 1200 Z"/>
  </svg>

  <div class="brand">
    <span class="brand-dot"></span>
    <span class="brand-name">CorvelPennix</span>
  </div>

  <div class="kicker">Inspirational</div>
  <h1 class="headline">ATHLETE</h1>
  <div class="tagline">VISITING OUR SCHOOL</div>

  <div class="role">
    <svg width="50" height="50" viewBox="0 0 44 44" aria-hidden="true">
      <g fill="none" stroke="#ffffff" stroke-width="2">
        <circle cx="22" cy="22" r="19"/>
        <path d="M22 3 c-6 8 -6 18 0 19 M22 22 c8 -2 15 2 18 7 M22 22 c-4 7 -12 11 -17 10"/>
      </g>
    </svg>
    <div class="role-text">Olympic<br>Volleyball Player</div>
  </div>

  <p class="bio">Marcus is a dynamic English volleyball player and coach, known for his leadership on and off the court and his passion for inspiring the next generation through sport.</p>

  <div class="athlete-name"><span>MARCUS</span></div>

  <h2 class="appeal">HELP US<br>RAISE FUNDS FOR<br>NEW SPORTS<br>EQUIPMENT</h2>

  <div class="value" style="left:359px; top:872px;">Be inspired</div>
  <div class="value" style="left:538px; top:858px;">Make a<br>difference</div>
  <div class="value" style="left:710px; top:852px;">Get Active</div>

  <div class="event-date">
    <svg class="event-date-panel" width="772" height="58" viewBox="0 0 772 58" aria-hidden="true">
      <path d="M0 0 H380 L345 58 H0 Z" fill="var(--royal)"/>
    </svg>
    <div class="event-date-label">
      <svg width="32" height="32" viewBox="0 0 32 32" aria-hidden="true">
        <g fill="none" stroke="#ffffff" stroke-width="1.8">
          <rect x="3" y="6" width="24" height="21" rx="2"/>
          <line x1="3" y1="12" x2="27" y2="12"/>
          <line x1="9" y1="3" x2="9" y2="8"/><line x1="21" y1="3" x2="21" y2="8"/>
          <circle cx="25" cy="25" r="5" fill="#2b2f8f"/>
          <path d="M22.5 25 l2 2 3 -4"/>
        </g>
      </svg>
      <span>Event Date</span>
    </div>
  </div>

  <p class="mission">Inspiring every child to lead an active, resilient and healthy life</p>
</main>
</body>
</html>
```